Create Vertical Dog Food Labels (3 inches x 5 inches) for PupKitchen

We need a packing Vertical label (3 inches x 5 inches) design for our line of Dog Food - Pup Kitchen at pupkitchenmeals.com (please review website). This design is for Custom Roll Labels. We have a logo already. Use our logo colors on label. What we need incorporated is a list of our ingredients:

50% Choice Beef
20% Pasture-raised Chicken
15% Brown Rice
15% Fresh Vegetables - Carrots, Kale, Zucchini
Herbal Health Boosters

We also need these lines at the bottom of the label:

Keeps in fridge for 4 days after thawing
Stores in freezer up to 6 months
Questions? email us at orders@meadowlanepantry.com

We have attached a sample of a competitor. The Kibble Crate.

Target Market(s)

Dog owners

Industry/Entity Type

Dog Food

Font styles to use
Sans Serif

Requirements
Must have
• Read project description above
Nice to have
• Our logo color incorporated
Should not have
• I want it simple.

```html
<!DOCTYPE html>
<html lang="en">
<head>
<meta charset="utf-8">
<title>PupKitchen Label</title>
<link href="https://fonts.googleapis.com/css2?family=Montserrat:wght@400;600;700&family=Oswald:wght@500&family=Fredoka:wght@600&display=swap" rel="stylesheet">
<style>
:root{
  --bg:#f1f1f1;
  --card:#ffffff;
  --green-dark:#0a6b0a;
  --green-mid:#4ea72c;
  --green-light:#84bf3f;
  --amber:#f7a400;
  --orange:#f05a28;
  --ink:#111111;
}
*{margin:0;padding:0;box-sizing:border-box}
html,body{width:1199px;height:1200px;overflow:hidden;background:var(--bg)}
.label{
  position:absolute;left:334px;top:163px;width:524px;height:873px;
  background:var(--card);border-radius:48px;overflow:hidden;
  font-family:'Montserrat',sans-serif;text-align:center;
}
.brand{position:absolute;top:140px;left:0;right:0;display:flex;justify-content:center;align-items:center;gap:10px}
.brand-dot{width:18px;height:18px;border-radius:50%;background:var(--green-light)}
.brand-name{font-family:'Montserrat',sans-serif;font-weight:700;font-size:25px;color:var(--green-dark)}
.hero{
  position:absolute;left:32px;top:205px;width:440px;height:372px;
  background:radial-gradient(ellipse at 60% 30%,#c9504a 0%,#e8b9b6 30%,#9ec66b 60%,#ffffff 78%);
}
.hero-disc{
  position:absolute;left:122px;top:245px;width:274px;height:274px;border-radius:50%;
  background:var(--card);display:flex;flex-direction:column;justify-content:center;align-items:center;
  font-family:'Fredoka',sans-serif;font-weight:600;font-size:30px;letter-spacing:3px;line-height:43px;
  color:var(--green-mid);
}
.hero-disc .strong{color:var(--green-dark)}
.ingredients{position:absolute;top:623px;left:0;right:0;font-family:'Oswald',sans-serif;font-weight:500;font-size:21px;line-height:33px;letter-spacing:-0.3px}
.sep{display:inline-block;width:2px;height:24px;vertical-align:-4px;margin:0 8px}
.c-dark{color:var(--green-dark)}.c-light{color:var(--green-light)}.c-amber{color:var(--amber)}.c-orange{color:var(--orange)}
.storage-row{position:absolute;top:708px;left:0;right:0;height:82px}
.tab{position:absolute;top:0;width:60px;height:80px}
.tab-left{left:0;background:var(--green-dark);border-radius:0 30px 30px 0}
.tab-right{right:0;background:var(--amber);border-radius:30px 0 0 30px;top:2px}
.storage{
  position:absolute;left:76px;width:372px;height:82px;border-radius:34px;background:var(--green-light);
  color:#fff;font-size:16.5px;line-height:26px;letter-spacing:.4px;display:flex;flex-direction:column;justify-content:center;
}
.contact{position:absolute;top:818px;left:0;right:0;font-size:15px;line-height:20px;color:var(--ink)}
.contact strong{font-weight:700;display:block}
</style>
</head>
<body>
<main class="label">
  <div class="brand"><span class="brand-dot"></span><span class="brand-name">PupKitchen</span></div>
  <div class="hero" role="img" aria-label="Photo of raw chicken, beef, carrots, kale and sliced zucchini arranged in a ring"></div>
  <div class="hero-disc">
    <span>HERBAL</span><span>HEALTH</span><span class="strong">BOOSTERS</span>
  </div>
  <div class="ingredients">
    <div><span class="c-dark">50% CHOICE BEEF</span><span class="sep" style="background:var(--green-dark)"></span><span class="c-light">20% PASTURE-RAISED CHICKEN</span></div>
    <div><span class="c-amber">15% BROWN RICE</span><span class="sep" style="background:var(--orange)"></span><span class="c-orange">15% FRESH VEGETABLES</span></div>
  </div>
  <div class="storage-row">
    <span class="tab tab-left"></span>
    <div class="storage"><span>Keeps in fridge for 4 days after thawing</span><span>Stores in freezer up to 6 months</span></div>
    <span class="tab tab-right"></span>
  </div>
  <p class="contact">Questions? email us at<strong>orders@meadowlanepantry.com</strong></p>
</main>
</body>
</html>
```